A start up special flyer design!

Hi All - Have updated the attachment content - This is the info required for the designs.
I need a catchy flyer to send out to a few areas to advertise the start of my plumbing business!
The flyer will contain an offer for customers, which will need to have some key details on it. See attached. Feel free to fit these criteria into the flyer given your knowledge on design and messaging principles. Key thing to get across to customers is the discount and special offer, and that it is a start up offer.
I have a logo that needs to be on the flyer as well - let me know what format you require and I will send through to you.
The color scheme needs to be blue / grey / black / white.
Let me know if you have any questions.
I

```html
<!DOCTYPE html>
<html lang="en">
<head>
<meta charset="utf-8">
<title>Harbour Line Plumbing – Start-Up Offer Flyer</title>
<link href="https://fonts.googleapis.com/css2?family=Oswald:wght@600;700&family=Mulish:wght@400;600;800&family=Montserrat:wght@700;800&family=Libre+Baskerville&display=swap" rel="stylesheet">
<style>
  :root{
    --blue:#0a66c8;
    --blue-deep:#0b4fa3;
    --black:#1b1b1d;
    --ink:#111;
    --white:#fff;
    --grey-light:#f1f1f2;
    --grey-mid:#d9dadc;
    --bar-grey:#9a9a9a;
    --stage:#e9e9ec;
  }
  *{margin:0;padding:0;box-sizing:border-box}
  html,body{width:1041px;height:1200px;overflow:hidden;background:var(--stage)}
  .canvas{position:relative;width:1041px;height:1200px;overflow:hidden}
  .flyer{
    position:absolute;left:96px;top:0;width:765px;height:1081px;
    transform:scale(1.1101);transform-origin:top left;
    background:linear-gradient(180deg,var(--grey-light) 40%,var(--grey-mid) 100%);
    overflow:hidden;font-family:"Mulish",sans-serif;color:var(--ink);
  }
  .abs{position:absolute}
  .photo-hero{left:0;top:0;width:765px;height:420px;
    background:linear-gradient(120deg,#f4f6f9 0%,#e3e8ee 35%,#8a9bb3 70%,#4f6d9e 100%)}
  .photo-worker{left:452px;top:545px;width:265px;height:395px;border-radius:6px;
    background:linear-gradient(180deg,#d7dade 0%,#26304a 45%,#1c2236 100%)}
  .shapes{left:0;top:0}
  .headline{left:42px;top:42px;font-family:"Oswald",sans-serif;font-weight:700;line-height:1;text-transform:uppercase}
  .headline .lead{font-size:31px;color:var(--ink);display:block;line-height:1.08}
  .headline .accent{font-size:60px;color:var(--blue);display:block;line-height:.85}
  .headline .accent.indent{padding-left:116px}
  .brand{left:50px;top:300px;color:var(--white);font-family:"Montserrat",sans-serif;font-weight:800;font-size:31px;line-height:1.35}
  .brand-tag{left:220px;top:388px;color:var(--white);font-family:"Libre Baskerville",serif;font-size:15px;width:168px;text-align:right}
  .offer-badge{left:467px;top:405px}
  .offer-word{left:467px;top:442px;width:252px;text-align:center;color:var(--white);font-family:"Montserrat",sans-serif;font-weight:800;font-size:54px}
  .rule{width:4px;background:var(--bar-grey)}
  .deal{left:57px;top:520px;color:var(--blue);font-family:"Oswald",sans-serif;font-weight:700;font-size:86px;line-height:1}
  .deal small{font-family:"Montserrat",sans-serif;font-weight:800;font-size:54px}
  .deal-sub{left:60px;top:603px;font-family:"Oswald",sans-serif;font-weight:700;font-size:52px;line-height:1;color:var(--ink)}
  .deal-sub sup{font-size:24px;vertical-align:22px}
  .perk{left:60px;font-weight:800;font-size:23px;line-height:1.3;color:var(--ink)}
  .appointment{left:0;top:893px;width:765px;height:188px}
  .appt-title{left:53px;top:907px;color:var(--white);font-family:"Oswald",sans-serif;font-weight:700;font-size:28px;letter-spacing:-.2px}
  .appt-text{left:53px;top:949px;color:var(--white);font-size:18px;line-height:1.3}
  .appt-text b{font-weight:800}
  .terms{right:40px;top:963px;color:var(--white);font-size:9.5px;line-height:1.38;text-align:right}
  .contact{color:var(--white);font-family:"Montserrat",sans-serif;font-weight:700;display:flex;align-items:center;gap:10px}
  .contact.phone{left:52px;top:1037px;font-size:27px}
  .contact.web{right:40px;top:1010px;font-size:18px}
  .contact.mail{right:40px;top:1052px;font-size:17px}
</style>
</head>
<body>
<div class="canvas">
  <main class="flyer">
    <div class="abs photo-hero" role="img" aria-label="Photo of a smiling plumber fitting pipes beneath a kitchen sink"></div>

    <svg class="abs shapes" width="765" height="520" viewBox="0 0 765 520">
      <polygon points="0,190 500,372 765,275 765,300 215,490 0,415" fill="var(--black)"/>
      <polygon points="215,490 765,282 765,300" fill="var(--white)"/>
      <polygon points="215,490 765,305 765,400 470,400 300,470" fill="var(--blue)"/>
      <polygon points="215,490 765,330 765,350 300,478" fill="var(--blue-deep)"/>
    </svg>

    <h1 class="abs headline">
      <span class="lead">Delivering quality</span>
      <span class="lead">work at a</span>
      <span class="accent">Decent</span>
      <span class="accent indent">Price</span>
    </h1>

    <div class="abs brand">HARBOUR LINE<br>PLUMBING</div>
    <div class="abs brand-tag">LOCAL PLUMBER</div>

    <svg class="abs offer-badge" width="252" height="155" viewBox="0 0 252 155">
      <polygon points="0,0 252,0 252,155 126,125 0,155" fill="var(--black)"/>
      <polyline points="8,0 8,143 126,114 244,143 244,0" fill="none" stroke="var(--blue)" stroke-width="1" stroke-dasharray="2 2"/>
    </svg>
    <div class="abs offer-word">OFFER</div>

    <div class="abs photo-worker" role="img" aria-label="Photo of a plumber holding a tap fitting and a red wrench"></div>

    <div class="abs rule" style="left:38px;top:530px;height:125px"></div>
    <div class="abs deal">15% <small>OFF</small></div>
    <div class="abs deal-sub">YOUR OVERALL BILL<sup>*</sup></div>

    <div class="abs rule" style="left:38px;top:688px;height:50px"></div>
    <p class="abs perk" style="top:683px">No Gst Payable, Saving You<br>Additional 10% On Your Bill<sup>^</sup></p>

    <div class="abs rule" style="left:38px;top:768px;height:80px"></div>
    <p class="abs perk" style="top:764px">Plus, A Free Hot Water<br>Health Check And<br>Replacement Quote~</p>

    <svg class="abs appointment" width="765" height="188" viewBox="0 0 765 188">
      <polygon points="0,0 385,0 432,47 765,47 765,188 0,188" fill="var(--black)"/>
      <polygon points="385,0 405,0 440,47 432,47" fill="var(--blue)"/>
      <polygon points="0,137 302,137 330,188 0,188" fill="var(--blue)"/>
      <polygon points="358,157 765,157 765,188 358,188" fill="var(--blue)"/>
    </svg>

    <div class="abs appt-title">TO MAKE AN APPOINTMENT</div>
    <p class="abs appt-text"><b>Call Or Email</b> Dean,<br>Or Alternatively Make A Booking<br>Directly On The <b>Website</b></p>
    <p class="abs terms">*Offer valid between 15 August 2016 to 15 October 2016<br>^Valid until 30 September 2016.<br>~Quote valid for 12 months from the quote date.</p>

    <div class="abs contact phone">
      <svg width="26" height="26" viewBox="0 0 24 24" aria-hidden="true"><circle cx="12" cy="12" r="10.5" fill="none" stroke="#fff" stroke-width="1.6"/><path d="M8.6 6.8l1.6-.4 1.1 2.6-1.2.9c.6 1.4 1.6 2.5 3 3.1l.9-1.2 2.6 1.1-.4 1.6c-.2.6-.8 1-1.4.9-3.4-.5-6.1-3.2-6.6-6.6-.1-.6.3-1.2.4-1.4z" fill="#fff"/></svg>
      0400 555 019
    </div>
    <div class="abs contact web">
      <svg width="18" height="18" viewBox="0 0 24 24" aria-hidden="true"><g fill="none" stroke="#fff" stroke-width="2"><circle cx="12" cy="12" r="10"/><ellipse cx="12" cy="12" rx="4.5" ry="10"/><line x1="2" y1="12" x2="22" y2="12"/></g></svg>
      www.harbourlineplumbing.com
    </div>
    <div class="abs contact mail">
      <svg width="22" height="16" viewBox="0 0 22 16" aria-hidden="true"><g fill="none" stroke="#fff" stroke-width="1.6"><rect x="1" y="1" width="20" height="14"/><polyline points="1,1 11,9 21,1"/></g></svg>
      dean@harbourlineplumbing.com
    </div>
  </main>
</div>
</body>
</html>
```